依頼詳細
◇デザインについて
・コーポレートカラーが赤なので、赤と白をメインカラーにしてデザインしていただきたいと思います。
・縦・横型どちらでも大丈夫です。

◆デザインする上で参考していただきたい事
・私たちは、コミュニケーションを改善するプロの集団です。
・私たちの仕事は、「身近な」コミュニケーションを改善することですが、提供しているサービスは「高品質」です。
→身近なものを扱っていますが、あまり安っぽくはしたくないです。

記載項目
◆表面
・肩書
・氏名
・ローマ字表記
・会社名
・郵便番号
・住所
・電話
・URL
・メールアドレス

◆裏面
・テキスト(私たちのミッション)(50W)
コミュニケーションを改善すること...のような内容が入ります。

◇どこかに
・会社ロゴ

希望イメージ
シンプル 複雑
単色 カラフル
暗い 明るい
日常 高級
遊び心 厳粛
未来的 伝統的
女性的 男性的
希望する色
赤系
納品ファイル
• イラストレーター形式 (.ai)
• フォトショップ形式 (.psd)
補足説明
データを納品頂いた後、こちらで従業員分複製いたしますので
編集可能なデータ(フォントデータ含む)をご納品いただきます。
具体的な記載内容

◆表面
・肩書:代表取締役CEO
・氏名:森下 啓介
・ローマ字表記:KEISUKE MORISHITA
・会社名:株式会社ルミヴェイル
・郵便番号:248-0036
・住所:神奈川県横浜市青葉区緑ヶ丘3-8-2-204
・電話:080-7163-2804
・URL:https://lumivale.jp/
・メールアドレス:morikei@lumivale.jp

◆裏面
・以下のテキスト(ミッション、missionなど付けてください。)
ユーザ視点を間近にすることで
コミュニケーションバグをなくし
価値が正しく伝わる社会を実現する

◇どこかに
・会社ロゴ(左端のキャラはトル可です)
◇デザインについて
ロゴ横のキャラが強く、これを使用するとどうしてもこのキャラのイメージに寄ってしまうので、キャラ無しバージョンがあると嬉しいです。

親しみやすいキャラクターデザインなのですが、
これがあると、どうしても、子供っぽく、安っぽく見えてしまうように思えます。

ロゴも丸いフォントなので、難しいとは思いますが...。

シンプルの中に小技が利いたデザインを希望します。
◇要素について
QRコードなど、こちらから指定した要素以外は不要です。
ほぼ文字要素なので、フォントの選定、配置、カーニングなど細部までデザインしていただきたいと思います。
■ 選んだ理由

全社員向けにアンケートをとった結果、
一番、多くの票が集まりましたデザインを選ばせていただきました。

■ 提案者全員のお礼・コメント

この度は、名刺デザインをご提案いただきありがとうございました。
こちらの想像を超えるデザイン案が、多く集まり
あたらめて会社の見え方を考える、よい機会になりました。

名刺以外もデザイン制作の機会はありますので、
今後とも、どうぞよろしくお願いいたします。

```html
<!DOCTYPE html>
<html lang="ja">
<head>
<meta charset="utf-8">
<title>名刺 表面 — 株式会社ルミヴェイル</title>
<link rel="stylesheet" href="https://fonts.googleapis.com/css2?family=Noto+Sans+JP:wght@400;500;700&display=swap">
<style>
  :root {
    --bg: #ececec;
    --card: #ffffff;
    --red: #d0121b;
    --ink: #222222;
    --ink-soft: #3a3a3a;
    --deco: #f0f0f0;
    --edge: #dddddd;
  }
  * { margin: 0; padding: 0; box-sizing: border-box; }
  html, body {
    width: 1200px; height: 1200px; overflow: hidden;
    background: var(--bg);
    font-family: "Noto Sans JP", sans-serif;
    color: var(--ink);
  }
  .card {
    position: absolute; left: 316px; top: 130px;
    width: 568px; height: 940px;
    background: var(--card);
    border: 1px solid var(--edge);
  }
  .corner-wedge { position: absolute; left: 0; top: 0; }
  .idea-illustration {
    position: absolute; left: 394px; top: 48px;
    width: 138px; height: 156px; border-radius: 50% 50% 40% 40%;
    background: radial-gradient(circle at 45% 40%, #f3f3f3, #f7f7f7 70%, transparent 72%);
  }
  .line { position: absolute; line-height: 1; white-space: nowrap; }
  .title { left: 82px; top: 192px; font-size: 17px; }
  .name { left: 80px; top: 224px; font-size: 40px; font-weight: 500; letter-spacing: 0.12em; }
  .romaji { left: 82px; top: 308px; font-size: 16px; letter-spacing: 0.02em; }
  .contact { left: 82px; display: flex; align-items: center; gap: 12px; font-size: 22px; color: var(--ink-soft); }
  .contact.phone { top: 368px; }
  .contact.mail { top: 420px; }
  .contact svg { width: 28px; height: 28px; flex: none; }
  .company { left: 151px; top: 638px; font-size: 20px; font-weight: 500; letter-spacing: 0.06em; }
  .postal { left: 151px; top: 682px; font-size: 16px; color: var(--ink-soft); }
  .address { left: 151px; top: 711px; font-size: 16px; color: var(--ink-soft); }
  .wordmark { left: 151px; top: 776px; font-size: 62px; font-weight: 700; letter-spacing: 0.01em; }
  .site { right: 57px; top: 857px; font-size: 21px; color: var(--red); }
</style>
</head>
<body>
  <div class="card">
    <svg class="corner-wedge" width="304" height="42" viewBox="0 0 304 42" aria-hidden="true">
      <polygon points="0,0 304,0 0,42" fill="var(--red)"/>
    </svg>
    <div class="idea-illustration" role="img" aria-label="淡いグレーの電球のイラスト"></div>

    <p class="line title">代表取締役&ensp;CEO</p>
    <p class="line name">森下 啓介</p>
    <p class="line romaji">KEISUKE MORISHITA</p>

    <p class="line contact phone">
      <svg viewBox="0 0 28 28" aria-hidden="true">
        <circle cx="14" cy="14" r="14" fill="var(--red)"/>
        <rect x="9.5" y="6.5" width="9" height="15" rx="1.6" fill="none" stroke="#fff" stroke-width="2"/>
      </svg>
      080-7163-2804
    </p>
    <p class="line contact mail">
      <svg viewBox="0 0 28 28" aria-hidden="true">
        <circle cx="14" cy="14" r="14" fill="var(--red)"/>
        <rect x="7" y="9" width="14" height="10" rx="1" fill="#fff"/>
        <polyline points="7.5,9.5 14,15 20.5,9.5" fill="none" stroke="var(--red)" stroke-width="1.6"/>
      </svg>
      morikei@lumivale.jp
    </p>

    <p class="line company">株式会社ルミヴェイル</p>
    <p class="line postal">〒248-0036</p>
    <p class="line address">神奈川県横浜市青葉区緑ヶ丘3-8-2-204</p>

    <p class="line wordmark">Lumivale</p>
    <p class="line site">https://lumivale.jp/</p>
  </div>
</body>
</html>
```